Brake Test Training for Coal Mining

We offer Brake Test Training for Coal Mine workers. It's a legislative requirement that workers who are tasked with performing brake testing have certain competencies to do so. We test Light Vehicles and trailers, Heavy Vehicles and Mobile Mining Equipment like Graders, Scrapers and Dump Trucks.

```html
<!DOCTYPE html>
<html lang="en">
<head>
<meta charset="utf-8">
<title>Brake Test Training for Coal Mine Workers</title>
<link rel="stylesheet" href="https://fonts.googleapis.com/css2?family=Oswald:wght@500;700&display=swap">
<style>
  :root {
    --yellow: #f8b91c;
    --black: #0d0d0d;
    --white: #ffffff;
    --navy: #14305a;
    --truck-tone-a: #c9a349;
    --truck-tone-b: #4a4128;
    --ute-tone-a: #f2f2f2;
    --ute-tone-b: #9a9ea3;
  }
  * { margin: 0; padding: 0; box-sizing: border-box; }
  html, body { width: 1200px; height: 962px; overflow: hidden; background: var(--white); }
  .billboard {
    position: relative; width: 1200px; height: 962px; overflow: hidden;
    background: var(--white); font-family: "Oswald", sans-serif;
  }
  .wave { position: absolute; inset: 0; width: 1200px; height: 962px; }
  .brand {
    position: absolute; left: 40px; top: 60px;
    display: flex; align-items: center; gap: 14px;
  }
  .brand-dot { width: 46px; height: 46px; border-radius: 50%; background: var(--navy); }
  .brand-name {
    font-weight: 700; font-size: 28px; line-height: 1.05; color: var(--navy);
    text-transform: uppercase; letter-spacing: 1px;
  }
  .headline {
    position: absolute; left: 38px; top: 150px;
    font-weight: 700; text-transform: uppercase; line-height: 1.05; letter-spacing: -1px;
  }
  .headline .lead { color: var(--yellow); font-size: 48px; display: block; }
  .headline .main { color: var(--black); font-size: 56px; display: block; }
  .headline .tail { color: var(--yellow); font-size: 56px; display: block; }
  .call-now {
    position: absolute; left: 185px; top: 350px;
    background: var(--yellow); color: var(--white);
    font-weight: 700; font-size: 30px; line-height: 1.3; text-transform: uppercase;
    padding: 4px 24px; border-radius: 12px;
    box-shadow: 4px 4px 0 var(--black);
  }
  .phone {
    position: absolute; left: 150px; top: 420px;
    font-weight: 700; font-size: 36px; line-height: 1.3; color: var(--black); letter-spacing: -0.5px;
  }
  .discount {
    position: absolute; left: 580px; top: 315px; width: 140px; height: 140px;
    border-radius: 50%; background: var(--black); border: 6px solid var(--white);
    display: flex; flex-direction: column; align-items: center; justify-content: center;
    font-weight: 700; line-height: 1;
  }
  .discount .amount { color: var(--white); font-size: 40px; }
  .discount .off { color: var(--yellow); font-size: 40px; }
  .photo { position: absolute; border-radius: 12px; }
  .photo-haul-truck {
    left: 685px; top: 20px; width: 480px; height: 270px;
    background: linear-gradient(160deg, var(--truck-tone-a), var(--truck-tone-b));
  }
  .photo-service-ute {
    left: 520px; top: 470px; width: 660px; height: 430px;
    background: linear-gradient(160deg, var(--ute-tone-a), var(--ute-tone-b));
  }
  .photo-loader {
    left: 10px; top: 700px; width: 450px; height: 240px;
    background: linear-gradient(160deg, var(--truck-tone-a), var(--truck-tone-b));
  }
</style>
</head>
<body>
<main class="billboard">
  <svg class="wave" viewBox="0 0 1200 962" aria-hidden="true">
    <path d="M0 600 C 260 620, 440 540, 580 430 C 720 330, 900 270, 1200 320 L1200 962 L0 962 Z" fill="var(--yellow)"/>
    <path d="M0 600 C 260 620, 440 540, 580 430 C 720 330, 900 270, 1200 320" fill="none" stroke="var(--black)" stroke-width="20"/>
  </svg>

  <div class="brand">
    <span class="brand-dot"></span>
    <span class="brand-name">Ridgeline<br>Operator Training</span>
  </div>

  <h1 class="headline">
    <span class="lead">We offer for</span>
    <span class="main">Brake Test Training</span>
    <span class="tail">Coal Mine Workers</span>
  </h1>

  <div class="call-now">Call Now</div>
  <div class="phone">000-0000-0000</div>

  <div class="photo photo-haul-truck" role="img" aria-label="Photo of a large yellow mining haul dump truck"></div>
  <div class="photo photo-service-ute" role="img" aria-label="Photo of a white mine-site service ute with crane tray"></div>
  <div class="photo photo-loader" role="img" aria-label="Photo of a yellow wheel loader beside a mining dump truck"></div>

  <div class="discount">
    <span class="amount">25%</span>
    <span class="off">OFF</span>
  </div>
</main>
</body>
</html>
```